Web Background Design Project

Hello,

We need some icons and a background image that is able to repeat it self on all sides.

It needs to match with: qpt.morvinholtworks.com

Thanks,
Bruno

```html
<!DOCTYPE html>
<html lang="en">
<head>
<meta charset="utf-8">
<title>Lumen Hill Chapel – Navigation</title>
<link rel="stylesheet" href="https://fonts.googleapis.com/css2?family=Montserrat:wght@500;800&display=swap">
<style>
  :root {
    --bg: #262626;
    --bg-edge: #1c1c1c;
    --text: #ffffff;
    --chrome-hi: #f4f4f4;
    --chrome-mid: #9a9a9a;
    --chrome-lo: #4a4a4a;
    --red-a: #c4161c; --red-b: #7a0a0c;
    --yellow-a: #e8c21a; --yellow-b: #c07a06;
    --green-a: #3fcc2a; --green-b: #0d8a0d;
    --purple-a: #8a2cd0; --purple-b: #3a0d82;
    --teal-a: #1aa6b8; --teal-b: #0b5e6c;
    --orange-a: #e2560c; --orange-b: #8a2c08;
    --icon: #ffffff;
    --screen: #0f5966;
  }
  * { margin: 0; padding: 0; box-sizing: border-box; }
  html, body { width: 1200px; height: 818px; overflow: hidden; }
  body {
    background: radial-gradient(ellipse at 50% 40%, var(--bg) 0%, var(--bg-edge) 100%);
    font-family: "Montserrat", sans-serif;
    color: var(--text);
    position: relative;
  }
  .brand {
    position: absolute; top: 66px; left: 0; width: 1200px;
    text-align: center;
    font-weight: 800; font-size: 30px; letter-spacing: 3px;
    line-height: 36px;
    color: var(--text);
  }
  .nav-item {
    position: absolute; width: 260px; margin-left: -130px;
    text-align: center; text-decoration: none; color: var(--text);
  }
  .tile {
    width: 202px; height: 202px; margin: 0 auto;
    border-radius: 36px; padding: 8px;
    background: linear-gradient(160deg, var(--chrome-hi) 0%, var(--chrome-mid) 35%, var(--chrome-lo) 55%, var(--chrome-hi) 75%, var(--chrome-mid) 100%);
    box-shadow: 0 10px 18px rgba(0,0,0,.7);
  }
  .tile-face {
    width: 100%; height: 100%; border-radius: 29px;
    position: relative; overflow: hidden;
    display: flex; align-items: center; justify-content: center;
    box-shadow: inset 0 0 10px rgba(0,0,0,.5);
  }
  .tile-face::after {
    content: ""; position: absolute; left: -30%; top: -60%;
    width: 170%; height: 120%; border-radius: 50%;
    background: linear-gradient(180deg, rgba(255,255,255,.22), rgba(255,255,255,.04));
    transform: rotate(-18deg); pointer-events: none;
  }
  .face-about   { background: linear-gradient(160deg, var(--red-a), var(--red-b)); }
  .face-history { background: linear-gradient(160deg, var(--yellow-a), var(--yellow-b)); }
  .face-mission { background: linear-gradient(160deg, var(--green-a), var(--green-b)); }
  .face-beliefs { background: linear-gradient(160deg, var(--purple-a), var(--purple-b)); }
  .face-media   { background: linear-gradient(160deg, var(--teal-a), var(--teal-b)); }
  .face-give    { background: linear-gradient(160deg, var(--orange-a), var(--orange-b)); }
  .icon { width: 140px; height: 140px; position: relative; z-index: 1; }
  .figure-area {
    position: relative; z-index: 1;
    width: 110px; height: 140px; border-radius: 40px 40px 14px 14px;
    background: linear-gradient(180deg, rgba(255,255,255,.85), rgba(255,255,255,.55));
  }
  .figure-area.group { width: 120px; height: 130px; background: linear-gradient(180deg, rgba(235,235,235,.9), rgba(170,170,170,.8)); }
  .figure-area.hand { width: 90px; height: 150px; border-radius: 50px 14px 40px 40px; }
  .figure-area.round { width: 136px; height: 136px; border-radius: 50%; }
  .figure-area.round.pale { background: linear-gradient(180deg, rgba(255,255,255,.6), rgba(255,255,255,.3)); }
  .label {
    display: block; margin-top: 18px;
    font-weight: 500; font-size: 28px; letter-spacing: 3px;
    line-height: 34px;
  }
  .col-1 { left: 234px; } .col-2 { left: 600px; } .col-3 { left: 971px; }
  .row-1 { top: 156px; } .row-2 { top: 461px; }
</style>
</head>
<body>
  <div class="brand">LUMEN HILL CHAPEL</div>

  <a class="nav-item col-1 row-1" href="#about">
    <div class="tile"><div class="tile-face face-about">
      <div class="figure-area group" role="img" aria-label="Silhouettes of three people standing together"></div>
    </div></div>
    <span class="label">ABOUT US</span>
  </a>

  <a class="nav-item col-2 row-1" href="#history">
    <div class="tile"><div class="tile-face face-history">
      <div class="figure-area round" role="img" aria-label="Clock illustration representing history"></div>
    </div></div>
    <span class="label">HISTORY</span>
  </a>

  <a class="nav-item col-3 row-1" href="#mission">
    <div class="tile"><div class="tile-face face-mission">
      <div class="figure-area round pale" role="img" aria-label="Target illustration representing mission"></div>
    </div></div>
    <span class="label">MISSION</span>
  </a>

  <a class="nav-item col-1 row-2" href="#beliefs">
    <div class="tile"><div class="tile-face face-beliefs">
      <div class="figure-area" role="img" aria-label="Silhouette of a seated statue in thought"></div>
    </div></div>
    <span class="label">BELIEFS</span>
  </a>

  <a class="nav-item col-2 row-2" href="#media">
    <div class="tile"><div class="tile-face face-media">
      <svg class="icon" viewBox="0 0 140 140" aria-hidden="true">
        <line x1="48" y1="8" x2="68" y2="30" stroke="var(--icon)" stroke-width="5"/>
        <line x1="92" y1="8" x2="72" y2="30" stroke="var(--icon)" stroke-width="5"/>
        <rect x="8" y="30" width="124" height="92" rx="10" fill="var(--icon)"/>
        <rect x="18" y="40" width="84" height="72" rx="14" fill="var(--screen)"/>
        <circle cx="117" cy="56" r="6" fill="var(--screen)"/>
        <circle cx="117" cy="76" r="6" fill="var(--screen)"/>
      </svg>
    </div></div>
    <span class="label">MEDIA</span>
  </a>

  <a class="nav-item col-3 row-2" href="#give">
    <div class="tile"><div class="tile-face face-give">
      <div class="figure-area hand" role="img" aria-label="Open hand reaching downward"></div>
    </div></div>
    <span class="label">GIVE</span>
  </a>
</body>
</html>
```